Social Media Graphics - Copperfield Loop

Create 6-7 individual social media graphics (square size) to encourage folks to join our online course, using either of the text below (only one set of text per graphic:

The Lantern Ridge Method
How to Create a 7-Figure Business From Scratch
Sign Up Today!

Or

The Lantern Ridge Method
Fast-track Your Way to a Multi-Million Business!
Sign Up Today!

For the color scheme of the graphics, use 1 or 2 colors in the color palette attached; or use any colors that look nice with their outfits; AVOID using red, white and blue altogether because it will look like an Independence Day (4th of July) graphic and we don’t want that; make sure the graphics appeal to both men and women

Make sure each graphic contains 1 of the 2 pics attached; and make sure one of the graphics is all TEXT only.

Target Market(s)

men and women looking to make more money

Industry/Entity Type

entrepreneurship

Requirements
Must have
• see the text document attached
Nice to have
• We are open to a nice color design; the color palette colors are not required, especially we don't want red, white and blue used together
Should not have
• AVOID using red, white and blue altogether because it will look like an Independence Day (4th of July) graphic and we dont want that

```html
<!DOCTYPE html>
<html lang="en">
<head>
<meta charset="utf-8">
<title>The Lantern Ridge Method – Social Graphics</title>
<link rel="stylesheet" href="https://fonts.googleapis.com/css2?family=Archivo+Black&family=Oswald:wght@600&display=swap">
<style>
  :root {
    --canvas: #000000;
    --pink: #f0215f;
    --pink-band: #f53d66;
    --pink-light: #fbc2d0;
    --pink-mid: #f36a8a;
    --blue: #0a3f82;
    --blue-title: #0b3d8f;
    --blue-light: #eef6fe;
    --blue-mid: #4e93d3;
    --gold: #f0b338;
    --ink: #2a2222;
    --white: #ffffff;
  }
  * { margin: 0; padding: 0; box-sizing: border-box; }
  html, body { width: 817px; height: 1200px; overflow: hidden; background: var(--canvas); }
  .sheet {
    position: relative; width: 817px; height: 1200px;
    display: grid;
    grid-template-columns: 380px 380px;
    grid-template-rows: 380px 380px 380px;
    column-gap: 14px; row-gap: 11px;
    padding: 20px 0 0 22px;
  }
  .tile { position: relative; overflow: hidden; }
  .tile--pink-photo { background: linear-gradient(180deg, var(--pink-light) 0%, #f7a2b6 45%, var(--pink-mid) 100%); }
  .tile--blue-photo { background: linear-gradient(180deg, var(--blue-light) 0%, #cfe4f8 45%, var(--blue-mid) 100%); }
  .tile--blue-text { background: var(--blue); }
  .tile--pink-text { background: var(--pink-band); }

  .torn { position: absolute; left: 0; width: 380px; display: block; }

  .title {
    position: absolute; left: 0; right: 0; text-align: center;
    font-family: "Archivo Black", sans-serif; text-transform: uppercase;
    line-height: 0.9; white-space: nowrap; letter-spacing: -0.5px;
  }
  .title .the { font-size: 28px; margin-right: 6px; }
  .title .big { font-size: 44px; }
  .title .line2 { display: block; font-size: 35px; margin-top: 2px; }
  .title--pink { color: var(--pink); }
  .title--blue { color: var(--blue-title); }
  .title--large .the { font-size: 34px; }
  .title--large .big { font-size: 54px; }
  .title--large .line2 { font-size: 43px; }

  .tagline {
    position: absolute; left: 0; right: 0; text-align: center;
    font-family: "Archivo Black", sans-serif; text-transform: uppercase;
    font-size: 12px; line-height: 1.25; letter-spacing: 0.3px;
  }
  .tagline--ink { color: var(--ink); }
  .tagline--gold { color: var(--gold); }
  .tagline--large { font-size: 15px; }

  .people {
    position: absolute; left: 95px; top: 150px; width: 210px; height: 230px;
    border-radius: 90px 90px 0 0;
  }
  .people--pink { background: linear-gradient(180deg, #c9566e 0%, #e0365f 55%, #3a2a2c 100%); opacity: 0.85; }
  .people--blue { background: linear-gradient(180deg, #6c5048 0%, #1e2a4a 50%, #1b4d8f 100%); opacity: 0.85; }

  .cta {
    position: absolute; left: 0; right: 0; text-align: center;
    font-family: "Oswald", sans-serif; font-weight: 600;
    font-size: 26px; letter-spacing: -0.8px; line-height: 1;
  }
  .cta--white { color: var(--white); }
  .cta--blue { color: var(--blue); }
  .cta--pink { color: var(--pink); }
  .cta--large { font-size: 31px; }
  .swoosh { display: block; margin: 2px auto 0; }
</style>
</head>
<body>
<main class="sheet">

  <!-- Pink, photo, "How to create" -->
  <section class="tile tile--pink-photo">
    <svg class="torn" style="top:245px" height="135" viewBox="0 0 380 135" aria-hidden="true">
      <path d="M0 8 L20 4 L40 9 L62 3 L85 8 L110 2 L140 7 L170 4 L200 9 L230 3 L262 8 L290 2 L318 7 L345 1 L380 5 L380 135 L0 135 Z" fill="var(--pink-band)" opacity="0.8"/>
    </svg>
    <div class="people people--pink" role="img" aria-label="Photo of the two course hosts standing together, smiling"></div>
    <h2 class="title title--pink" style="top:22px"><span class="the">The</span><span class="big">Lantern</span><span class="line2">Ridge Method</span></h2>
    <p class="tagline tagline--ink" style="top:112px">How to create a 7-figure business<br>from scratch</p>
    <p class="cta cta--white" style="top:328px">Sign Up Today!
      <svg class="swoosh" width="70" height="8" viewBox="0 0 70 8" aria-hidden="true"><path d="M2 7 Q30 1 68 3" stroke="var(--white)" stroke-width="2.5" fill="none" stroke-linecap="round"/></svg></p>
  </section>

  <!-- Blue, photo, "Fast-track" -->
  <section class="tile tile--blue-photo">
    <svg class="torn" style="top:235px" height="145" viewBox="0 0 380 145" aria-hidden="true">
      <path d="M0 10 L25 5 L50 10 L80 4 L110 9 L140 3 L170 8 L200 4 L230 9 L260 2 L290 7 L320 3 L350 8 L380 2 L380 145 L0 145 Z" fill="var(--blue-mid)" opacity="0.85"/>
    </svg>
    <div class="people people--blue" role="img" aria-label="Photo of the two course hosts standing together, smiling"></div>
    <h2 class="title title--blue" style="top:20px"><span class="the">The</span><span class="big">Lantern</span><span class="line2">Ridge Method</span></h2>
    <p class="tagline tagline--gold" style="top:108px">Fast-track your way to a<br>multi-million business!</p>
    <p class="cta cta--white" style="top:326px">Sign Up Today!
      <svg class="swoosh" width="70" height="8" viewBox="0 0 70 8" aria-hidden="true"><path d="M2 7 Q30 1 68 3" stroke="var(--white)" stroke-width="2.5" fill="none" stroke-linecap="round"/></svg></p>
  </section>

  <!-- Blue, text only -->
  <section class="tile tile--blue-text">
    <svg class="torn" style="top:40px" height="280" viewBox="0 0 380 280" aria-hidden="true">
      <path d="M0 12 L18 6 L40 9 L62 3 L90 7 L120 2 L150 6 L180 3 L210 6 L240 2 L270 5 L300 1 L330 5 L360 2 L380 6 L380 258 L355 262 L330 256 L300 262 L270 258 L240 265 L210 259 L180 266 L150 260 L120 266 L90 261 L60 268 L30 263 L0 270 Z" fill="var(--white)"/>
    </svg>
    <h2 class="title title--blue title--large" style="top:84px"><span class="the">The</span><span class="big">Lantern</span><span class="line2">Ridge Method</span></h2>
    <p class="tagline tagline--gold tagline--large" style="top:200px">Fast-track your way to a<br>multi-million business!</p>
    <p class="cta cta--blue cta--large" style="top:252px">Sign Up Today!
      <svg class="swoosh" width="80" height="8" viewBox="0 0 80 8" aria-hidden="true"><path d="M2 7 Q34 1 78 3" stroke="var(--blue)" stroke-width="2.5" fill="none" stroke-linecap="round"/></svg></p>
  </section>

  <!-- Pink, text only -->
  <section class="tile tile--pink-text">
    <svg class="torn" style="top:40px" height="280" viewBox="0 0 380 280" aria-hidden="true">
      <path d="M0 12 L18 6 L40 9 L62 3 L90 7 L120 2 L150 6 L180 3 L210 6 L240 2 L270 5 L300 1 L330 5 L360 2 L380 6 L380 258 L355 262 L330 256 L300 262 L270 258 L240 265 L210 259 L180 266 L150 260 L120 266 L90 261 L60 268 L30 263 L0 270 Z" fill="var(--white)"/>
    </svg>
    <h2 class="title title--pink title--large" style="top:84px"><span class="the">The</span><span class="big">Lantern</span><span class="line2">Ridge Method</span></h2>
    <p class="tagline tagline--ink tagline--large" style="top:200px">How to create a 7-figure business<br>from scratch</p>
    <p class="cta cta--pink cta--large" style="top:252px">Sign Up Today!
      <svg class="swoosh" width="80" height="8" viewBox="0 0 80 8" aria-hidden="true"><path d="M2 7 Q34 1 78 3" stroke="var(--pink)" stroke-width="2.5" fill="none" stroke-linecap="round"/></svg></p>
  </section>

  <!-- Pink, photo, "Fast-track" -->
  <section class="tile tile--pink-photo">
    <svg class="torn" style="top:245px" height="135" viewBox="0 0 380 135" aria-hidden="true">
      <path d="M0 8 L20 4 L40 9 L62 3 L85 8 L110 2 L140 7 L170 4 L200 9 L230 3 L262 8 L290 2 L318 7 L345 1 L380 5 L380 135 L0 135 Z" fill="var(--pink-band)" opacity="0.8"/>
    </svg>
    <div class="people people--pink" role="img" aria-label="Photo of the two course hosts standing together, smiling"></div>
    <h2 class="title title--pink" style="top:22px"><span class="the">The</span><span class="big">Lantern</span><span class="line2">Ridge Method</span></h2>
    <p class="tagline tagline--ink" style="top:112px">Fast-track your way to a<br>multi-million business!</p>
    <p class="cta cta--white" style="top:328px">Sign Up Today!
      <svg class="swoosh" width="70" height="8" viewBox="0 0 70 8" aria-hidden="true"><path d="M2 7 Q30 1 68 3" stroke="var(--white)" stroke-width="2.5" fill="none" stroke-linecap="round"/></svg></p>
  </section>

  <!-- Blue, photo, "How to create" -->
  <section class="tile tile--blue-photo">
    <svg class="torn" style="top:235px" height="145" viewBox="0 0 380 145" aria-hidden="true">
      <path d="M0 10 L25 5 L50 10 L80 4 L110 9 L140 3 L170 8 L200 4 L230 9 L260 2 L290 7 L320 3 L350 8 L380 2 L380 145 L0 145 Z" fill="var(--blue-mid)" opacity="0.85"/>
    </svg>
    <div class="people people--blue" role="img" aria-label="Photo of the two course hosts standing together, smiling"></div>
    <h2 class="title title--blue" style="top:20px"><span class="the">The</span><span class="big">Lantern</span><span class="line2">Ridge Method</span></h2>
    <p class="tagline tagline--gold" style="top:108px">How to create a 7-figure business<br>from scratch</p>
    <p class="cta cta--white" style="top:326px">Sign Up Today!
      <svg class="swoosh" width="70" height="8" viewBox="0 0 70 8" aria-hidden="true"><path d="M2 7 Q30 1 68 3" stroke="var(--white)" stroke-width="2.5" fill="none" stroke-linecap="round"/></svg></p>
  </section>

</main>
</body>
</html>
```